Upcoming lecture sponsored by a church on an important topic

We have a Reformation The Speech coming up at the end of October on the topic of law and gospel. I thought it might be cool to use a flyer that looks like it was from that day and age. Picture what Conrad Velmer would advertise things on kind of an old church/reformation type format. It will be sponsored by our church, and we have a paragraph or two to describe the lecture that would be included on the flyer. We would also want it formatted so that it could be printed on postcards and mailed to churches and individuals.

The flyer should have the following paragraph...

The distinction between the law and the gospel is the most important distinction in the Christian faith. Conrad Velmer: “Distinguishing between the law and the gospel is the highest art in Christendom, one who every person who values the name Christian ought to recognize, know, and possess.” The distinction between the law and the gospel is of great comfort for the child of God. “For the law was given by Moses, but grace and truth came by Jesus Christ” (John 1:17). For these reasons, the distinction between the law and the gospel is the most heavily assaulted doctrine in the Christian faith. This Reformation Day, join us for an explanation and defense of the great distinction between God’s good law and God’s glorious gospel.

And the flyer should have the following information...

Topic: The Steady Word and the Bright Promise
Date and Time: Tuesday, October 31, 2023 at 7:30pm
Host: Harrow Creek Fellowship Church
Speaker: Rev. Gerald Voskuil
Venue: The Marlow Hall, 5172 Brenton Avenue, Hudsonville, MI 49318
Format: Lecture followed by Q&A and refreshments

00AB8E
00BBA5
67D7C9
C6EFE9
E9F9F6

• The color scheme that I would like to have is a teal color (the same color as found at www.brackenhollowchapel.com

```html
<!DOCTYPE html>
<html lang="en">
<head>
<meta charset="utf-8">
<title>Reformation Day Lecture</title>
<link rel="stylesheet" href="https://fonts.googleapis.com/css2?family=Oswald:wght@300;400&family=Source+Sans+3:ital,wght@0,300;0,400;0,700;1,700&display=swap">
<style>
  :root {
    --panel: #225464;
    --quote-box: #45b0bf;
    --topic: #4fb3c8;
    --label: #4dd4e8;
    --mark: #55dde8;
    --white: #ffffff;
  }
  * { margin: 0; padding: 0; box-sizing: border-box; }
  html, body { width: 848px; height: 1200px; overflow: hidden; background: var(--panel); }
  .flyer {
    position: relative; width: 848px; height: 1200px; overflow: hidden;
    background: var(--panel);
    font-family: "Source Sans 3", "Source Sans Pro", sans-serif;
    color: var(--white);
  }
  .photo-vault {
    position: absolute; left: 523px; top: 0; width: 325px; height: 748px;
    background: linear-gradient(180deg, #a8683c 0%, #d99a62 25%, #b87b4e 45%, #e2b486 70%, #f0d2b0 100%);
  }
  .photo-nave {
    position: absolute; left: 523px; top: 748px; width: 325px; height: 452px;
    background: linear-gradient(180deg, #e9dcd6 0%, #f6eef0 45%, #d9ccca 75%, #5a4a48 100%);
  }
  .headline {
    position: absolute; left: 52px; top: 38px;
    font-family: "Oswald", sans-serif; font-weight: 300;
    font-size: 82px; line-height: 1; letter-spacing: 3px;
  }
  .topic {
    position: absolute; left: 53px; top: 158px;
    font-family: "Oswald", sans-serif; font-weight: 300;
    font-size: 40px; line-height: 52px; color: var(--topic);
  }
  .speaker {
    position: absolute; left: 54px; top: 290px;
    font-weight: 700; font-size: 20px; letter-spacing: 1.8px;
  }
  .quote-box {
    position: absolute; left: 0; top: 363px; width: 686px; height: 385px;
    background: var(--quote-box);
  }
  .quote-mark { position: absolute; }
  .quote-mark.open { left: 36px; top: 14px; }
  .quote-mark.close { left: 443px; top: 340px; }
  .quote-text {
    position: absolute; left: 53px; top: 23px;
    font-weight: 300; font-size: 17.2px; line-height: 27.7px; letter-spacing: 0.45px;
  }
  .quote-text span { display: block; white-space: nowrap; }
  .quote-text .first { padding-left: 48px; }
  .details { position: absolute; left: 61px; top: 777px; }
  .detail { margin-bottom: 34px; }
  .label {
    font-style: italic; font-weight: 700; font-size: 20px; line-height: 34px;
    color: var(--label);
  }
  .value { font-weight: 700; font-size: 20px; line-height: 34px; }
  .address { font-weight: 400; font-size: 20px; line-height: 34px; }
</style>
</head>
<body>
<main class="flyer">
  <div class="photo-vault" role="img" aria-label="Photograph of a church's vaulted ceiling with warm lit pointed arches"></div>
  <div class="photo-nave" role="img" aria-label="Photograph of a bright church interior with tall windows and a choir at the front"></div>

  <h1 class="headline">JOIN US !</h1>
  <h2 class="topic">Topic : The Steady Word and<br>the Bright Promise</h2>
  <p class="speaker">SPEAKER : REV. GERALD VOSKUIL</p>

  <section class="quote-box">
    <svg class="quote-mark open" width="48" height="34" viewBox="0 0 48 34" aria-hidden="true">
      <path fill="var(--mark)" d="M11 34C4 34 0 29 0 22 0 10 8 2 19 0l1 4C13 6 9 10 9 15c1-1 2-1 4-1 6 0 10 4 10 10s-5 10-12 10zm25 0c-7 0-11-5-11-12C25 10 33 2 44 0l1 4c-7 2-11 6-11 11 1-1 2-1 4-1 6 0 10 4 10 10s-5 10-12 10z"/>
    </svg>
    <p class="quote-text">
      <span class="first">The distinction between the law and the gospel is the most</span>
      <span>important distinction in the Christian faith. Conrad Velmer:</span>
      <span>“Distinguishing between the law and the gospel is the highest art</span>
      <span>in Christendom, one who every person who values the name</span>
      <span>Christian ought to recognize, know, and possess.” The distinction</span>
      <span>between the law and the gospel is of great comfort for the child of</span>
      <span>God. “For the law was given by Moses, but grace and truth came</span>
      <span>by Jesus Christ” (John 1:17). For these reasons, the distinction</span>
      <span>between the law and the gospel is the most heavily assaulted</span>
      <span>doctrine in the Christian faith. This Reformation Day, join us for</span>
      <span>an explanation and defense of the great distinction between</span>
      <span>God’s good law and God’s glorious gospel.</span>
    </p>
    <svg class="quote-mark close" width="48" height="34" viewBox="0 0 48 34" aria-hidden="true">
      <path fill="var(--mark)" transform="rotate(180 24 17)" d="M11 34C4 34 0 29 0 22 0 10 8 2 19 0l1 4C13 6 9 10 9 15c1-1 2-1 4-1 6 0 10 4 10 10s-5 10-12 10zm25 0c-7 0-11-5-11-12C25 10 33 2 44 0l1 4c-7 2-11 6-11 11 1-1 2-1 4-1 6 0 10 4 10 10s-5 10-12 10z"/>
    </svg>
  </section>

  <section class="details">
    <div class="detail">
      <p class="label">Date and Time</p>
      <p class="value">Tuesday, October 31, 2023 at 7:30pm</p>
    </div>
    <div class="detail">
      <p class="label">Host &amp; Venue</p>
      <p class="value">Harrow Creek Fellowship Church</p>
      <p class="address">The Marlow Hall, 5172 Brenton Avenue,</p>
      <p class="address">Hudsonville, MI 49318</p>
    </div>
    <div class="detail">
      <p class="label">Format</p>
      <p class="value">Lecture followed by Q&amp;A &amp; refreshments</p>
    </div>
  </section>
</main>
</body>
</html>
```